Studying Effectively To Do List

I am looking to design a new "Study To Do List" for High School students (Ages 15 - 18) . This will be printed as an A4 notepad and so should only be a single A4 page.

The Design will need to be professional and look semi-serious but also be appealing to High school students (Ages 15 - 18) and should NOT be gender specific.

I have attached a word document outlining the structure of the page. The space provided should be large enough that people can write in it comfortably.

The notepad will most likely be printed in black and white but I'm also looking at coloured options - colours should be kept to a minimum.

This will be printed professionally and should also include a 3mm bleed.

The design should also include the business logo (included in the word document)

Target Market(s)

High School students (Ages 15 - 18). Both genders

Industry/Entity Type

Education

Font styles to use
Serif
Sans Serif

Requirements
Must have
• Please see the word document attached.
Should not have
• Too much colour

```html
<!DOCTYPE html>
<html lang="en">
<head>
<meta charset="utf-8">
<title>Study To Do List</title>
<link href="https://fonts.googleapis.com/css2?family=Share+Tech+Mono&family=Orbitron:wght@700&display=swap" rel="stylesheet">
<style>
  :root{
    --brand:#e94e0b;
    --paper:#ffffff;
    --ink:#1c1c1c;
    --muted:#7a7a7a;
    --rule:#8e8e8e;
  }
  *{box-sizing:border-box;margin:0;padding:0}
  html,body{width:849px;height:1200px;overflow:hidden}
  body{background:var(--brand);position:relative;font-family:"Share Tech Mono",monospace;color:var(--ink)}
  .card{position:absolute;background:var(--paper);border-radius:4px}
  .brand-box{left:344px;top:45px;width:81px;height:81px;display:flex;flex-direction:column;align-items:center;justify-content:center;gap:5px}
  .brand-dot{width:22px;height:22px;border-radius:50%;background:var(--brand)}
  .brand-name{font-size:11px;letter-spacing:1px;text-align:center;line-height:1.1;color:var(--ink)}
  .date-box{left:440px;top:45px;width:370px;height:81px}
  .date-label{position:absolute;left:17px;top:22px;font-family:"Orbitron",sans-serif;font-weight:700;font-size:16px;letter-spacing:3px}
  .date-line{position:absolute;left:17px;right:35px;top:59px;border-bottom:1px dashed var(--rule)}
  .revision{left:42px;top:142px;width:768px;height:120px}
  .homework{left:42px;top:268px;width:768px;height:371px}
  .assessments{left:42px;top:645px;width:768px;height:371px}
  .notes{left:42px;top:1023px;width:768px;height:133px}
  .side-label{position:absolute;font-size:13px;letter-spacing:4px;white-space:nowrap;transform:translate(-50%,-50%) rotate(-90deg)}
  .rule{position:absolute;height:0;border-bottom:1px solid var(--rule)}
  .num{position:absolute;font-size:12px;transform:translateY(-100%);padding-bottom:1px}
  .field{position:absolute;font-size:13px;letter-spacing:2px;transform:translateY(-100%);padding-bottom:2px}
  .field.muted{color:var(--muted)}
  .field.sub{letter-spacing:2.5px}
  .arrow{font-size:11px;margin-right:6px}
</style>
</head>
<body>

<div class="card brand-box">
  <div class="brand-dot"></div>
  <div class="brand-name">KESTREL<br>LEARNING</div>
</div>

<div class="card date-box">
  <div class="date-label">DATE:</div>
  <div class="date-line"></div>
</div>

<section class="card revision">
  <div class="side-label" style="left:16px;top:60px">REVISION</div>
  <span class="num" style="left:47px;top:26px">1</span><div class="rule" style="left:47px;width:335px;top:26px"></div>
  <span class="num" style="left:47px;top:52px">2</span><div class="rule" style="left:47px;width:335px;top:52px"></div>
  <span class="num" style="left:47px;top:79px">3</span><div class="rule" style="left:47px;width:335px;top:79px"></div>
  <span class="num" style="left:47px;top:105px">4</span><div class="rule" style="left:47px;width:335px;top:105px"></div>
  <span class="num" style="left:398px;top:26px">5</span><div class="rule" style="left:398px;width:335px;top:26px"></div>
  <span class="num" style="left:398px;top:52px">6</span><div class="rule" style="left:398px;width:335px;top:52px"></div>
  <span class="num" style="left:398px;top:79px">7</span><div class="rule" style="left:398px;width:335px;top:79px"></div>
  <span class="num" style="left:398px;top:105px">8</span><div class="rule" style="left:398px;width:335px;top:105px"></div>
</section>

<section class="card homework">
  <div class="side-label" style="left:16px;top:85px">HOMEWORK</div>

  <span class="field muted" style="left:47px;top:32px">SUBJECT</span><div class="rule" style="left:47px;width:686px;top:32px"></div>
  <span class="field" style="left:47px;top:61px"><span class="arrow">↗</span>TASK</span><div class="rule" style="left:156px;width:577px;top:61px"></div>

  <span class="field muted" style="left:47px;top:89px">SUBJECT</span><div class="rule" style="left:47px;width:686px;top:89px"></div>
  <span class="field" style="left:47px;top:118px"><span class="arrow">↗</span>TASK</span><div class="rule" style="left:156px;width:577px;top:118px"></div>

  <span class="field muted" style="left:47px;top:147px">SUBJECT</span><div class="rule" style="left:47px;width:686px;top:147px"></div>
  <span class="field" style="left:47px;top:176px"><span class="arrow">↗</span>TASK</span><div class="rule" style="left:156px;width:577px;top:176px"></div>

  <span class="field muted" style="left:47px;top:204px">SUBJECT</span><div class="rule" style="left:47px;width:686px;top:204px"></div>
  <span class="field" style="left:47px;top:233px"><span class="arrow">↗</span>TASK</span><div class="rule" style="left:156px;width:577px;top:233px"></div>

  <span class="field muted" style="left:47px;top:261px">SUBJECT</span><div class="rule" style="left:47px;width:686px;top:261px"></div>
  <span class="field" style="left:47px;top:290px"><span class="arrow">↗</span>TASK</span><div class="rule" style="left:156px;width:577px;top:290px"></div>

  <span class="field muted" style="left:47px;top:319px">SUBJECT</span><div class="rule" style="left:47px;width:686px;top:319px"></div>
  <span class="field" style="left:47px;top:348px"><span class="arrow">↗</span>TASK</span><div class="rule" style="left:156px;width:577px;top:348px"></div>
</section>

<section class="card assessments">
  <div class="side-label" style="left:16px;top:136px">ASSESSMENTS</div>

  <span class="field muted" style="left:47px;top:36px">ASSESSMENT</span><div class="rule" style="left:47px;width:439px;top:36px"></div>
  <span class="field" style="left:490px;top:36px">DUE</span><div class="rule" style="left:521px;width:212px;top:36px"></div>
  <span class="field" style="left:47px;top:65px"><span class="arrow">↗</span>ELEMENT</span><div class="rule" style="left:156px;width:577px;top:65px"></div>

  <span class="field muted" style="left:47px;top:93px">ASSESSMENT</span><div class="rule" style="left:47px;width:439px;top:93px"></div>
  <span class="field" style="left:490px;top:93px">DUE</span><div class="rule" style="left:521px;width:212px;top:93px"></div>
  <span class="field" style="left:47px;top:122px"><span class="arrow">↗</span>ELEMENT</span><div class="rule" style="left:156px;width:577px;top:122px"></div>

  <span class="field muted" style="left:47px;top:150px">ASSESSMENT</span><div class="rule" style="left:47px;width:439px;top:150px"></div>
  <span class="field" style="left:490px;top:150px">DUE</span><div class="rule" style="left:521px;width:212px;top:150px"></div>
  <span class="field" style="left:47px;top:179px"><span class="arrow">↗</span>ELEMENT</span><div class="rule" style="left:156px;width:577px;top:179px"></div>

  <span class="field muted" style="left:47px;top:208px">ASSESSMENT</span><div class="rule" style="left:47px;width:439px;top:208px"></div>
  <span class="field" style="left:490px;top:208px">DUE</span><div class="rule" style="left:521px;width:212px;top:208px"></div>
  <span class="field" style="left:47px;top:237px"><span class="arrow">↗</span>ELEMENT</span><div class="rule" style="left:156px;width:577px;top:237px"></div>

  <span class="field muted" style="left:47px;top:265px">ASSESSMENT</span><div class="rule" style="left:47px;width:439px;top:265px"></div>
  <span class="field" style="left:490px;top:265px">DUE</span><div class="rule" style="left:521px;width:212px;top:265px"></div>
  <span class="field" style="left:47px;top:294px"><span class="arrow">↗</span>ELEMENT</span><div class="rule" style="left:156px;width:577px;top:294px"></div>

  <span class="field muted" style="left:47px;top:322px">ASSESSMENT</span><div class="rule" style="left:47px;width:439px;top:322px"></div>
  <span class="field" style="left:490px;top:322px">DUE</span><div class="rule" style="left:521px;width:212px;top:322px"></div>
  <span class="field" style="left:47px;top:351px"><span class="arrow">↗</span>ELEMENT</span><div class="rule" style="left:156px;width:577px;top:351px"></div>
</section>

<section class="card notes">
  <div class="side-label" style="left:16px;top:74px">NOTES</div>
  <span class="num" style="left:40px;top:35px">1</span><div class="rule" style="left:40px;width:160px;top:35px"></div>
  <span class="num" style="left:40px;top:62px">2</span><div class="rule" style="left:40px;width:160px;top:62px"></div>
  <span class="num" style="left:40px;top:88px">3</span><div class="rule" style="left:40px;width:160px;top:88px"></div>
  <span class="num" style="left:40px;top:116px">4</span><div class="rule" style="left:40px;width:160px;top:116px"></div>
  <span class="num" style="left:216px;top:35px">5</span><div class="rule" style="left:216px;width:160px;top:35px"></div>
  <span class="num" style="left:216px;top:62px">6</span><div class="rule" style="left:216px;width:160px;top:62px"></div>
  <span class="num" style="left:216px;top:88px">7</span><div class="rule" style="left:216px;width:160px;top:88px"></div>
  <span class="num" style="left:216px;top:116px">8</span><div class="rule" style="left:216px;width:160px;top:116px"></div>
  <div class="rule" style="left:398px;width:335px;top:35px"></div>
  <div class="rule" style="left:398px;width:335px;top:62px"></div>
  <div class="rule" style="left:398px;width:335px;top:88px"></div>
  <div class="rule" style="left:398px;width:335px;top:116px"></div>
  <div class="side-label" style="left:752px;top:74px">PRACTICE</div>
</section>

</body>
</html>
```